Rework of existing brochure designs

Replace Logo(s) with images provided
Company and website
Minor changes in text

-------------
Second file (Harbor Keystone) to be redesigned into same design as Velmix Brochure

Did not get the level of creative reequired

```html
<!DOCTYPE html>
<html lang="en">
<head>
<meta charset="utf-8">
<title>SkyMentors Services Sheet</title>
<link href="https://fonts.googleapis.com/css2?family=Open+Sans:wght@400;600&family=Raleway:wght@500;600&display=swap" rel="stylesheet">
<style>
  :root {
    --backdrop: #1f7fcf;
    --paper: #f1f1f3;
    --brand-blue: #1d62ad;
    --band-blue: #1a5ea9;
    --ink: #2b2b2b;
    --ink-soft: #3a3a3a;
    --badge-grey: #dcdcdf;
  }
  * { margin: 0; padding: 0; box-sizing: border-box; }
  html, body { width: 1200px; height: 1013px; overflow: hidden; }
  body {
    background: var(--backdrop);
    font-family: "Open Sans", Arial, sans-serif;
    color: var(--ink);
  }
  .sheet {
    position: absolute;
    left: 267px; top: 30px;
    width: 665px; height: 953px;
    background: var(--paper);
    box-shadow: 0 12px 40px rgba(0, 30, 80, 0.35);
  }
  .divider {
    position: absolute;
    left: 217px; top: 90px;
    width: 1.5px; height: 482px;
    background: var(--brand-blue);
  }
  .service-title {
    position: absolute;
    left: 61px;
    width: 140px;
    font-family: "Raleway", Arial, sans-serif;
    font-weight: 600;
    font-size: 12.5px;
    line-height: 14.5px;
    letter-spacing: 0.2px;
    text-transform: uppercase;
    color: var(--brand-blue);
  }
  .service-highlights {
    position: absolute;
    left: 61px;
    width: 145px;
    list-style: none;
    font-size: 10px;
    line-height: 13.6px;
    color: var(--ink-soft);
  }
  .service-highlights li {
    position: relative;
    padding-left: 13px;
    margin-bottom: 2px;
  }
  .service-highlights li::before,
  .scope-list li::before {
    content: "•";
    position: absolute;
    left: 0;
  }
  .service-detail {
    position: absolute;
    left: 250px;
    width: 390px;
    font-size: 11.5px;
    line-height: 15.5px;
    color: var(--ink);
  }
  .service-detail p { margin-bottom: 9px; }
  .scope-list {
    list-style: none;
    margin-top: 12px;
  }
  .scope-list li {
    position: relative;
    padding-left: 15px;
    height: 19.2px;
  }
  .quick-win .service-title { top: 100px; }
  .quick-win .service-highlights { top: 126px; }
  .quick-win .service-detail { top: 101px; }
  .assurance .service-title { top: 384px; }
  .assurance .service-highlights { top: 428px; }
  .assurance .service-detail { top: 385px; }
  .about {
    position: absolute;
    left: 48px; top: 812px;
    width: 414px;
    font-size: 10px;
    line-height: 13.6px;
    text-align: justify;
    color: var(--ink-soft);
  }
  .about h2 {
    font-family: "Raleway", Arial, sans-serif;
    font-weight: 600;
    font-size: 10.5px;
    color: var(--ink);
    margin-bottom: 2px;
  }
  .partner-badge {
    position: absolute;
    left: 485px; top: 830px;
    width: 136px; height: 39px;
    border-radius: 3px;
    background: var(--badge-grey);
  }
  .contact-band {
    position: absolute;
    left: 0; bottom: 0;
    width: 100%; height: 31px;
    background: var(--band-blue);
    display: flex;
    justify-content: space-between;
    align-items: center;
    padding: 0 46px 0 48px;
    font-family: "Raleway", Arial, sans-serif;
    font-weight: 500;
    font-size: 11px;
    color: #ffffff;
    letter-spacing: 0.2px;
  }
</style>
</head>
<body>
  <main class="sheet">
    <div class="divider"></div>

    <section class="service quick-win">
      <h2 class="service-title">One Day Quick Win</h2>
      <ul class="service-highlights">
        <li>Solutions Improvement</li>
        <li>Knowledge Share</li>
        <li>Investigate Complimentary Solutions</li>
        <li>Configuration Health Check</li>
        <li>Post Implementation Refinements</li>
        <li>Process Improvement</li>
      </ul>
      <div class="service-detail">
        <p>Get up and running in a day with this fast track configuration.<br>Everything you need to be maximising your ROI from day one!</p>
        <p>Scope: Everything we can get done one day. Choose from some of these.</p>
        <ul class="scope-list">
          <li>Campaign Design and Flow</li>
          <li>Lead Smart List management and status updates</li>
          <li>Build Landing Pages and Forms</li>
          <li>Track Web Page Visitor behaviour</li>
          <li>Drip feed email marketing and responses</li>
          <li>Measure Campaign Results</li>
          <li>Integrate with Orbitforce.com</li>
          <li>Build Knowledge</li>
        </ul>
      </div>
    </section>

    <section class="service assurance">
      <h2 class="service-title">Harbor<br>Keystone</h2>
      <ul class="service-highlights">
        <li>Build an extended support package that is tailored to your level of expertise and goals</li>
        <li>Maintain and grow adoption and secure the future of your Velmix solution and maximise your ROI</li>
      </ul>
      <div class="service-detail">
        <p>A flexible monthly solution based support plan tailored to your<br>unique requirements.</p>
        <p>Scope: Total flexibility for tailor made solutions support.</p>
        <ul class="scope-list">
          <li>Service Level Agreements</li>
          <li>Dedicated Solutions Administrator</li>
          <li>Regular Solution Health Check</li>
          <li>Knowledge Share</li>
          <li>Solutions Enhancements</li>
          <li>Telephone Assistance</li>
        </ul>
      </div>
    </section>

    <section class="about">
      <h2>About SkyMentors</h2>
      <p>Created in 2009, SkyMentors are one of the longest established Orbitforce.com partners in the UK with a history of over 25 years in business management consulting, business process improvement and now Cloud Transformation and innovation. We provide dynamic and trust worthy advice, knowledge and expertise with a range of different consulting styles to complement your organisation's personality and aspirations.</p>
    </section>

    <div class="partner-badge" role="img" aria-label="Registered consulting partner badge"></div>

    <footer class="contact-band">
      <span class="phone">0800 555 0199</span>
      <span class="website">www.skymentors.co.uk</span>
    </footer>
  </main>
</body>
</html>
```